New Australian Beverage Company Needs a Bottle Label Design

We are after a bottle label design for our new aloe vera drinks called 'Sun Ridge'.

There are 5+ different colourrs we would like to compliment the flavors.

We are after a logo that is simple and eye catching.
Updates

Project Deadline Extended Reason: Business partner is currently overseas and would like to review all designs with him upon his return. Added Thursday, May 14, 2015

Project Deadline Extended Reason: We have received a number of great designs and we require more time to decide which direction we would like to take our label design. Thank you for your understanding. Added Thursday, May 21, 2015

Target Market(s)

Our target market is open for all as we would like to supply our drinks to quench everyone's thirst, however our biggest customers would be the teenagers to adults up to around the age of 50.

Industry/Entity Type

It Company

Requirements
Must have
• We are after a refreshing label that catches the eyes and makes you feel like picking it up and drinking it.

```html
<!DOCTYPE html>
<html lang="en">
<head>
<meta charset="utf-8">
<title>Sun Ridge Aloe Vera – Flavour Labels</title>
<link rel="stylesheet" href="https://fonts.googleapis.com/css2?family=Open+Sans:wght@700;800&display=swap">
<style>
  :root {
    --brand-green: #22cc00;
    --badge-text: #ffffff;
    --citrus: #ccff00;
    --berry: #e0c2fb;
    --peach: #ffc4c2;
    --page: #ffffff;
  }
  html, body {
    margin: 0;
    padding: 0;
    width: 1200px;
    height: 1000px;
    overflow: hidden;
    background: var(--page);
  }
  .label-sheet {
    display: block;
    width: 1200px;
    height: 1000px;
  }
  .label-outline {
    stroke: var(--brand-green);
    stroke-width: 6;
  }
  .label--citrus .label-outline { fill: var(--citrus); }
  .label--berry .label-outline { fill: var(--berry); }
  .label--peach .label-outline { fill: var(--peach); }
  .badge-shape { fill: var(--brand-green); }
  .badge-text {
    font-family: "Open Sans", Arial, sans-serif;
    font-weight: 800;
    fill: var(--badge-text);
    text-anchor: middle;
  }
  .badge-text--claim { font-size: 19px; letter-spacing: -0.3px; }
  .badge-text--flavour { font-size: 30px; }
  .brand-name, .product-name {
    font-family: "Open Sans", Arial, sans-serif;
    font-weight: 800;
    fill: var(--brand-green);
    text-anchor: middle;
  }
  .brand-name { font-size: 44px; }
  .product-name { font-size: 42px; }
  .plant-art { fill: url(#plant-glow); }
  .plant-glow-core { stop-color: var(--brand-green); stop-opacity: 0.75; }
  .plant-glow-mid { stop-color: var(--brand-green); stop-opacity: 0.35; }
  .plant-glow-edge { stop-color: var(--brand-green); stop-opacity: 0; }
</style>
</head>
<body>
<svg class="label-sheet" viewBox="0 0 1200 1000" xmlns="http://www.w3.org/2000/svg">
  <defs>
    <radialGradient id="plant-glow" cx="50%" cy="62%" r="55%">
      <stop class="plant-glow-core" offset="0"/>
      <stop class="plant-glow-mid" offset="0.55"/>
      <stop class="plant-glow-edge" offset="1"/>
    </radialGradient>
  </defs>

  <g class="label label--citrus" transform="translate(258 465)">
    <ellipse class="label-outline" cx="0" cy="0" rx="151" ry="265"/>
    <ellipse class="badge-shape" cx="0" cy="-203" rx="73" ry="27"/>
    <text class="badge-text badge-text--claim" x="0" y="-196">ALL NATURAL</text>
    <text class="brand-name" x="0" y="-110">Sun Ridge</text>
    <ellipse class="plant-art" cx="0" cy="-4" rx="124" ry="90" role="img" aria-label="Illustration of an aloe vera plant with white-edged green leaves"/>
    <text class="product-name" x="0" y="132">aloe vera</text>
    <ellipse class="badge-shape" cx="0" cy="195" rx="83" ry="29"/>
    <text class="badge-text badge-text--flavour" x="0" y="206">CITRUS</text>
  </g>

  <g class="label label--berry" transform="translate(603 465)">
    <ellipse class="label-outline" cx="0" cy="0" rx="151" ry="265"/>
    <ellipse class="badge-shape" cx="0" cy="-203" rx="73" ry="27"/>
    <text class="badge-text badge-text--claim" x="0" y="-196">ALL NATURAL</text>
    <text class="brand-name" x="0" y="-110">Sun Ridge</text>
    <ellipse class="plant-art" cx="0" cy="-4" rx="124" ry="90" role="img" aria-label="Illustration of an aloe vera plant with white-edged green leaves"/>
    <text class="product-name" x="0" y="132">aloe vera</text>
    <ellipse class="badge-shape" cx="0" cy="195" rx="83" ry="29"/>
    <text class="badge-text badge-text--flavour" x="0" y="206">BERRY</text>
  </g>

  <g class="label label--peach" transform="translate(945 465)">
    <ellipse class="label-outline" cx="0" cy="0" rx="151" ry="265"/>
    <ellipse class="badge-shape" cx="0" cy="-203" rx="73" ry="27"/>
    <text class="badge-text badge-text--claim" x="0" y="-196">ALL NATURAL</text>
    <text class="brand-name" x="0" y="-110">Sun Ridge</text>
    <ellipse class="plant-art" cx="0" cy="-4" rx="124" ry="90" role="img" aria-label="Illustration of an aloe vera plant with white-edged green leaves"/>
    <text class="product-name" x="0" y="132">aloe vera</text>
    <ellipse class="badge-shape" cx="0" cy="195" rx="83" ry="29"/>
    <text class="badge-text badge-text--flavour" x="0" y="206">PEACH</text>
  </g>

</svg>
</body>
</html>
```